University Entrepreneurship Housing Cohort Needs a Flyer Design

Wrenfield College's Venture and Discovery Center needs a flyer designed for their new "V-Nest" (short for Venture Nest) Living Learning Community.

The purpose of the V-Nest Residential Cohort (RC) is to provide students at Wrenfield College with the opportunity to live, learn, and participate in activities that have an entrepreneurship and innovation focus. Students with entrepreneurial ambitions will be able to connect with others who share those similar interests and aspirations. The community will create a space for students to learn about entrepreneurial and innovative ways of thinking and working, and to begin to implement their ideas using RC provided resources (e.g,, workshops, site visits, mentors, and peer-networking). The RC will also include an on-site V-Nest Commons, which functions as a study space for V-Nest students. The lounge will have dry-erase walls, a 65-inch touch screen monitor, internet connectivity, and printing capabilities. The final design should communicate an exciting and innovative focused opportunity for young college students.

Note: Both logos need to be on the flyer, but pictures can be selected additionally as desired.

Target Market(s)

Undergraduate students who plan to live in on campus housing and have an interest in entrepreneurship and innovation

Industry/Entity Type

University

Font styles to use
Sans Serif

Requirements
Must have
• Both logos need to be on the flyer, but pictures can be selected additionally as desired.
• Font: Gill Sans (for larger text) and Usherwood (for smaller text)
• The purpose of the Venture Nest (V-Nest) Living Learning Community (RC) is to provide students at Wrenfield College with the opportunity to live, learn, and participate in activities that have an entrepreneurship and innovation focus.
• Students with entrepreneurial ambitions will be able to connect with others who share similar interests and aspirations. Using resources provided by the V-Nest RC and the Venture and Discovery Center, residents will begin to develop their ideas, as well as participate in experiences that include workshops, competitions, mentorship, exposure to the Atlanta ecosystem, and peer-to-peer networking.
• The V-Nest Commons will include:
• - Collaborative study space
• - Dry-erase walls
• - 65-inch touchscreen monitor
• - Internet connectivity
• - Printing capabilities
• Website: vdc.wrenfield-example.edu
• Phone: 555-208-3164
• Twitter: @WCVDCtr
• Facebook: WC_VDCtr
• LinkedIn: Venture & Discovery Center at Wrenfield College
Nice to have
• Color codes:
• Blue PMS 286
• RED PMS 186
• Grey PMS 404
• More details here: http://brandpack.wrenfield-example.edu/guidelines/visual-identity/type-color-usage/

```html
<!DOCTYPE html>
<html lang="en">
<head>
<meta charset="utf-8">
<title>Introducing the V-Nest</title>
<link rel="stylesheet" href="https://fonts.googleapis.com/css2?family=Lato:wght@300;400;700;900&display=swap">
<style>
  :root {
    --brand-blue: #0033a0;
    --bar-blue: #1a4cc8;
    --bar-blue-dark: #0d36a0;
    --brand-red: #c8102e;
    --warm-grey: #776e64;
    --ink: #2a2a2a;
    --paper: #f4f4f4;
    --frame-dark: #2e2e30;
  }
  * { box-sizing: border-box; margin: 0; padding: 0; }
  html, body { width: 849px; height: 1200px; overflow: hidden; background: #ffffff; }
  .flyer {
    position: relative;
    width: 849px;
    height: 1200px;
    overflow: hidden;
    background: linear-gradient(100deg, #ffffff 0%, var(--paper) 55%, #e4e4e4 100%);
    font-family: "Lato", sans-serif;
    color: var(--ink);
  }
  .collage { position: absolute; left: 330px; top: 0; width: 519px; height: 1200px; }

  .program-mark {
    position: absolute; left: 64px; top: 70px;
    display: flex; flex-direction: column; align-items: center; gap: 18px;
    width: 290px;
  }
  .program-mark__dot { width: 120px; height: 120px; border-radius: 50%; background: var(--brand-blue); }
  .program-mark__name { font-size: 30px; font-weight: 700; color: var(--brand-blue); letter-spacing: 0.5px; }

  .headline {
    position: absolute; left: 56px; top: 372px;
    font-weight: 700; font-size: 56px; line-height: 1.06; letter-spacing: 0.5px;
    color: var(--ink); text-transform: uppercase;
  }
  .headline__program { color: var(--brand-red); text-transform: none; }

  .features-intro { position: absolute; left: 58px; top: 585px; font-size: 30px; color: var(--ink); }
  .feature-list { position: absolute; left: 56px; top: 640px; list-style: none; }
  .feature-list__item {
    height: 42px; margin-bottom: 14px;
    display: flex; align-items: center; padding-left: 14px;
    background: linear-gradient(180deg, var(--bar-blue) 0%, var(--bar-blue-dark) 100%);
    clip-path: polygon(0 0, calc(100% - 22px) 0, 100% 50%, calc(100% - 22px) 100%, 0 100%);
    color: #ffffff; font-size: 23px; letter-spacing: 0.5px;
    text-transform: uppercase; white-space: nowrap;
  }
  .feature-list__item--w1 { width: 440px; }
  .feature-list__item--w2 { width: 500px; }
  .feature-list__item--w3 { width: 400px; }
  .feature-list__item--w4 { width: 410px; }

  .purpose {
    position: absolute; left: 200px; top: 862px; width: 330px;
    font-size: 17px; line-height: 1.32; color: var(--ink);
  }
  .purpose strong { font-weight: 700; color: var(--brand-red); }

  .sponsor { position: absolute; left: 40px; top: 1004px; display: flex; align-items: center; gap: 18px; }
  .sponsor__mark { display: flex; align-items: center; gap: 12px; }
  .sponsor__square { width: 28px; height: 28px; background: var(--brand-blue); }
  .sponsor__name { font-size: 31px; font-weight: 700; color: var(--brand-blue); line-height: 1.05; width: 140px; }
  .sponsor__rule { width: 2px; height: 80px; background: var(--warm-grey); }
  .sponsor__unit { font-size: 23px; color: var(--warm-grey); line-height: 1.25; text-transform: uppercase; letter-spacing: 0.3px; }

  .contact {
    position: absolute; left: 58px; top: 1098px;
    display: grid; grid-template-columns: 84px auto; row-gap: 2px;
    font-size: 16px; line-height: 18px;
  }
  .contact__label { font-weight: 700; color: var(--ink); }
  .contact__value { color: var(--warm-grey); }
</style>
</head>
<body>
<main class="flyer">

  <svg class="collage" viewBox="0 0 519 1200" xmlns="http://www.w3.org/2000/svg">
    <defs>
      <linearGradient id="tone-office" x1="0" y1="0" x2="1" y2="1"><stop offset="0" stop-color="#b7b2a8"/><stop offset="1" stop-color="#5b5650"/></linearGradient>
      <linearGradient id="tone-study" x1="0" y1="0" x2="1" y2="1"><stop offset="0" stop-color="#e2d3c4"/><stop offset="1" stop-color="#9c7b6a"/></linearGradient>
      <linearGradient id="tone-red" x1="0" y1="0" x2="1" y2="1"><stop offset="0" stop-color="#8a3a36"/><stop offset="1" stop-color="#2c1c1c"/></linearGradient>
      <linearGradient id="tone-laptop" x1="0" y1="0" x2="1" y2="1"><stop offset="0" stop-color="#d9c48a"/><stop offset="1" stop-color="#4a3a2c"/></linearGradient>
      <linearGradient id="tone-lounge" x1="0" y1="0" x2="1" y2="1"><stop offset="0" stop-color="#c9cdd2"/><stop offset="1" stop-color="#6d5148"/></linearGradient>
      <linearGradient id="tone-hall" x1="0" y1="0" x2="1" y2="1"><stop offset="0" stop-color="#d6d2cc"/><stop offset="1" stop-color="#7b756d"/></linearGradient>
    </defs>
    <polygon points="170,0 519,0 519,1200 170,1200 430,560" fill="#e6e6e6"/>
    <polygon points="250,0 519,0 519,1200 300,1200 519,560" fill="var(--frame-dark)" opacity="0.9"/>
    <polygon points="260,0 519,0 519,200 380,150" fill="url(#tone-office)" role="img" aria-label="Photo: student working on a laptop in a window-lit lounge"/>
    <polygon points="40,215 215,60 385,210 205,385" fill="url(#tone-study)" stroke="#ffffff" stroke-width="6" role="img" aria-label="Photo: smiling student at a dry-erase wall during a group discussion"/>
    <polygon points="385,215 519,210 519,430 430,420" fill="url(#tone-red)" role="img" aria-label="Photo: student seated in a red-walled study area"/>
    <polygon points="250,430 415,290 519,380 519,560 380,600" fill="url(#tone-laptop)" stroke="#ffffff" stroke-width="6" role="img" aria-label="Photo: student with a laptop in a collaborative space"/>
    <polygon points="420,600 519,560 519,700 450,690" fill="url(#tone-red)" role="img" aria-label="Photo: student on a phone at a study table"/>
    <polygon points="230,760 400,650 519,720 519,930 300,960" fill="url(#tone-lounge)" stroke="#ffffff" stroke-width="6" role="img" aria-label="Photo: students relaxing on sofas in the commons lounge"/>
    <polygon points="230,1040 519,940 519,1200 190,1200" fill="url(#tone-hall)" stroke="#ffffff" stroke-width="6" role="img" aria-label="Photo: students gathered in a residence hall common area"/>
  </svg>

  <div class="program-mark">
    <div class="program-mark__dot"></div>
    <div class="program-mark__name">V-Nest</div>
  </div>

  <h1 class="headline">Introducing<br>The <span class="headline__program">V-Nest</span></h1>

  <p class="features-intro">The lounge will have..</p>
  <ul class="feature-list">
    <li class="feature-list__item feature-list__item--w1">Dry-erase walls</li>
    <li class="feature-list__item feature-list__item--w2">A 65-inch touch screen monitor</li>
    <li class="feature-list__item feature-list__item--w3">Internet connectivity</li>
    <li class="feature-list__item feature-list__item--w4">Printing capabilities</li>
  </ul>

  <p class="purpose">The purpose of the <strong>V-Nest</strong> Residential Cohort (RC) is to provide undergraduate students at Wrenfield College with the opportunity to live, learn, and participate in activities that have an entrepreneurship and innovation focus.</p>

  <div class="sponsor">
    <div class="sponsor__mark">
      <div class="sponsor__square"></div>
      <div class="sponsor__name">Wrenfield College</div>
    </div>
    <div class="sponsor__rule"></div>
    <div class="sponsor__unit">Venture and<br>Discovery Center</div>
  </div>

  <dl class="contact">
    <dt class="contact__label">Website</dt><dd class="contact__value">vdc.wrenfield-example.edu</dd>
    <dt class="contact__label">Phone</dt><dd class="contact__value">555-208-3164</dd>
    <dt class="contact__label">Twitter</dt><dd class="contact__value">@WCVDCtr</dd>
    <dt class="contact__label">Facebook</dt><dd class="contact__value">WC_VDCtr</dd>
  </dl>

</main>
</body>
</html>
```